Nine Lanterns Rollup Banner/Poster

I provide a Personalised Baby Planning and Maternity Concierge service and I will have a couple of Trade Fair events this year for which I'd like to have a roll-up banner/poster designed. In a nutshell, Nine Lanterns is a Baby Planning service that helps busy moms and dads by providing guidance, support and education to them in a tailored and unbiased manner. Think of us as a personal assistant in all things pregnancy-related. The company colour schemes can be found on our website at http://www.ninelanterns.com.sg - I also have business cards and brochures and can share these designs with you so you get the idea.
--------------------------------------------------------------
TEXT to be on the poster:

The arrival of a new baby can be both exciting and stressful. Let us guide you in making the decisions that are best for your family.

Nine Lanterns is a Baby Planning service that helps busy moms and dads by providing guidance, support and education to them in a tailored and unbiased manner. Think of us as your personal assistant in all things pregnancy-related. Enjoy your pregnancy journey and make well-informed decisions with confidence, but without the stress!

www.ninelanterns.com.sg

An idea would be to have a picture of a mom (of Asian origin) with some thought bubbles containing text like:
- Baby names?
- Birth planning?
- Childbirth classes?
- Baby products?
- Childcare options?
- Full month planning?

Hope it doesn't get too crowded - if it does, we can discuss some changes!

Regards,
Corinne
www.ninelanterns.com.sg
Updates

Hi all, Thanks for the first few designs. I think perhaps all that text might be too crowded. Perhaps better to propose design only with the following text: -------------------- The arrival of a new baby can be both exciting and stressful. Let us guide you in making the decisions that are best for your family. www.ninelanterns.com.sg -------------------- The thought bubbles can remain - I like them! :-)

Hi as another note - I noticed everyone submitted designs only using the TEAL colour. There's also a small touch of pink on my website.... could you incorporate that in the design in a subtle way somewhere please? That would be nice :-)

Target Market(s)

My target market are pregnant moms! Especially first-time moms.

Industry/Entity Type

Education

Requirements
Must have
• The poster size must be 200cm tall x 85cm wide. There needs to be some margin or bleed area of course. The resolution needs to be a minimum of 300 dpi at actual size.

Please keep to the Nine Lanterns colour scheme provided in the attached images (business card and brochures).

```html
<!DOCTYPE html>
<html lang="en">
<head>
<meta charset="utf-8">
<title>Nine Lanterns – Roll-up Banner</title>
<link rel="stylesheet" href="https://fonts.googleapis.com/css2?family=Comfortaa:wght@700&family=Tinos&family=Roboto+Condensed:wght@700&family=Open+Sans:ital,wght@1,700&display=swap">
<style>
  :root {
    --paper: #ffffff;
    --ink: #3f3f3f;
    --ink-soft: #6b6b6b;
    --teal: #4fbfbd;
    --teal-light: #a6e2e1;
    --teal-dark: #2f9c9b;
    --pink: #e7879b;
    --title-box: #f1f1f1;
    --bubble-coral: #e2836f;
    --bubble-blush: #f2bcbc;
    --bubble-sky: #a7cdee;
    --bubble-olive: #c5c999;
    --bubble-aqua: #84d1cf;
    --bubble-rose: #ee9fb0;
  }
  * { margin: 0; padding: 0; box-sizing: border-box; }
  html, body { width: 1200px; height: 2824px; overflow: hidden; background: var(--paper); }
  .banner { position: relative; width: 1200px; height: 2824px; background: var(--paper); overflow: hidden; }

  .title-box {
    position: absolute; left: 59px; top: 35px; width: 1059px; height: 318px;
    background: var(--title-box);
    display: flex; align-items: center; justify-content: center;
  }
  .brand-name {
    font-family: "Comfortaa", sans-serif; font-weight: 700;
    font-size: 138px; color: var(--ink); letter-spacing: -2px;
  }

  .mother-photo {
    position: absolute; left: 0; top: 365px; width: 682px; height: 1376px;
    background: linear-gradient(160deg, #f4e4d8 0%, #e9cdb9 30%, #9fd0e6 55%, #7cc0df 80%, #c9b8cf 100%);
  }

  .intro {
    position: absolute; left: 560px; width: 640px; top: 585px;
    text-align: center; font-family: "Tinos", serif; color: var(--ink-soft);
    font-size: 54px; line-height: 1.3;
  }
  .intro .feelings { font-size: 68px; margin-top: 6px; }
  .teal { color: var(--teal); }
  .pink { color: var(--pink); }

  .bubbles { position: absolute; left: 0; top: 0; width: 1200px; height: 1600px; }
  .bubble-text {
    font-family: "Open Sans", sans-serif; font-style: italic; font-weight: 700;
    font-size: 36px; fill: #2d2d2d; text-anchor: middle;
  }

  .url-ribbon { position: absolute; left: 0; top: 1720px; width: 1200px; height: 290px; }
  .url-text {
    position: absolute; left: 0; top: 1745px; width: 965px; height: 190px;
    display: flex; align-items: center; justify-content: center;
    font-family: "Roboto Condensed", sans-serif; font-weight: 700;
    font-size: 72px; color: #ffffff;
  }

  .closing {
    position: absolute; left: 0; top: 2060px; width: 1200px;
    text-align: center; font-family: "Tinos", serif; color: var(--ink);
    font-size: 64px; line-height: 141px;
  }
  .closing .guide { font-size: 126px; color: var(--teal); }
  .closing .family { font-size: 132px; color: var(--pink); }

  .contact {
    position: absolute; left: 62px; top: 2555px;
    font-family: "Tinos", serif; font-size: 33px; color: var(--ink);
    list-style: none;
  }
  .contact li { display: flex; align-items: center; height: 64px; }
  .contact svg { width: 40px; height: 40px; margin-right: 22px; flex: none; }
</style>
</head>
<body>
<main class="banner">
  <header class="title-box">
    <h1 class="brand-name">Nine Lanterns</h1>
  </header>

  <div class="mother-photo" role="img" aria-label="Photo of a smiling pregnant mother in a light blue top, cradling her belly"></div>

  <p class="intro">The arrival of a new<br>baby can be both<br><span class="feelings"><span class="teal">exciting</span> &amp; <span class="pink">stressful</span></span></p>

  <svg class="bubbles" viewBox="0 0 1200 1600" aria-hidden="false">
    <g class="bubble bubble--products">
      <path d="M600 1060 L585 1100 L640 1068 Z" fill="var(--bubble-coral)"/>
      <ellipse cx="653" cy="995" rx="102" ry="76" fill="var(--bubble-coral)"/>
      <text class="bubble-text" x="653" y="985">Baby</text>
      <text class="bubble-text" x="653" y="1030">products?</text>
    </g>
    <g class="bubble bubble--classes">
      <path d="M900 1040 L960 1075 L930 1030 Z" fill="var(--bubble-blush)"/>
      <ellipse cx="880" cy="982" rx="132" ry="72" fill="var(--bubble-blush)" stroke="#f7d3d3" stroke-width="8" stroke-dasharray="14 6"/>
      <text class="bubble-text" x="880" y="970" style="font-size:33px">Childbirth</text>
      <text class="bubble-text" x="880" y="1012" style="font-size:33px">classes?</text>
    </g>
    <g class="bubble bubble--birth">
      <path d="M1000 1200 L990 1245 L1040 1205 Z" fill="var(--bubble-sky)"/>
      <ellipse cx="1035" cy="1128" rx="150" ry="96" fill="var(--bubble-sky)"/>
      <text class="bubble-text" x="1045" y="1118">Birth</text>
      <text class="bubble-text" x="1045" y="1164">planning?</text>
    </g>
    <g class="bubble bubble--childcare">
      <path d="M470 1230 L455 1275 L510 1238 Z" fill="var(--bubble-olive)"/>
      <ellipse cx="612" cy="1192" rx="190" ry="56" fill="var(--bubble-olive)"/>
      <text class="bubble-text" x="612" y="1205">Childcare options?</text>
    </g>
    <g class="bubble bubble--fullmonth">
      <path d="M760 1380 L745 1425 L800 1388 Z" fill="var(--bubble-aqua)"/>
      <ellipse cx="924" cy="1318" rx="206" ry="92" fill="var(--bubble-aqua)"/>
      <text class="bubble-text" x="930" y="1308">Full month</text>
      <text class="bubble-text" x="930" y="1354">planning?</text>
    </g>
    <g class="bubble bubble--names">
      <path d="M610 1500 L620 1545 L650 1505 Z" fill="var(--bubble-rose)"/>
      <ellipse cx="665" cy="1456" rx="148" ry="64" fill="var(--bubble-rose)"/>
      <text class="bubble-text" x="665" y="1470">Baby names?</text>
    </g>
  </svg>

  <svg class="url-ribbon" viewBox="0 0 1200 290" aria-hidden="true">
    <defs>
      <linearGradient id="ribbonBand" x1="0" y1="0" x2="0" y2="1">
        <stop offset="0" stop-color="#b4e8e7"/>
        <stop offset="0.5" stop-color="#7fd3d2"/>
        <stop offset="1" stop-color="#4fbfbd"/>
      </linearGradient>
      <linearGradient id="ribbonTail" x1="0" y1="0" x2="1" y2="0">
        <stop offset="0" stop-color="#5cc4c3"/>
        <stop offset="1" stop-color="#a6e2e1"/>
      </linearGradient>
    </defs>
    <polygon points="870,70 1155,70 1060,170 1155,268 870,268" fill="url(#ribbonTail)"/>
    <polygon points="870,214 965,214 965,268" fill="var(--teal-dark)"/>
    <rect x="0" y="25" width="965" height="189" fill="url(#ribbonBand)"/>
    <rect x="0" y="25" width="965" height="14" fill="#d3f2f1"/>
  </svg>
  <p class="url-text">www.ninelanterns.com.sg</p>

  <p class="closing">Let us <span class="guide">guide</span> you in<br>the decisions that are<br>best for your <span class="family">family.</span></p>

  <ul class="contact">
    <li>
      <svg viewBox="0 0 40 40" aria-hidden="true"><rect x="12" y="6" width="16" height="30" rx="3" fill="none" stroke="var(--ink)" stroke-width="3"/><rect x="16" y="11" width="8" height="9" fill="var(--ink)"/><line x1="14" y1="2" x2="14" y2="7" stroke="var(--ink)" stroke-width="3"/></svg>
      +65 8123 4409
    </li>
    <li>
      <svg viewBox="0 0 40 40" aria-hidden="true"><rect x="5" y="12" width="30" height="20" rx="2" fill="none" stroke="var(--ink)" stroke-width="3"/><polyline points="5,13 20,24 35,13" fill="none" stroke="var(--ink)" stroke-width="3"/></svg>
      corinne@ninelanterns.com.sg
    </li>
    <li>
      <svg viewBox="0 0 40 40" aria-hidden="true"><path d="M20 37 C10 24 8 20 8 15 A12 12 0 0 1 32 15 C32 20 30 24 20 37 Z" fill="none" stroke="var(--ink)" stroke-width="3"/><circle cx="20" cy="15" r="4.5" fill="var(--ink)"/></svg>
      12 Lantern Grove, Singapore 417302
    </li>
  </ul>
</main>
</body>
</html>
```